Silver Kettle Consulting

I need a business card design and for my consulting business. I provide outsourced CFO services for start-ups and high growth companies. I call my company Silver Kettle because building a company is similar to building a stone pathway, selecting each stone and planning several stones head in order to properly place them - all while keeping an eye on the final design and curve of the path. The underlying idea I want to express with my marketing images is that I'm someone that you can count on to help build your business and be there step by step to help. I'm not the old gray-haired CFO that many folks think of. :) I've included a one-page summery that I'm working on, it includes a summary of what I do. I've used a muted pathway and with greens in the header , and do like the green, but am open to other colors if they work well. Would like something that looks like a pathway, but a more abstract version instead of a picture.

Marketing

```html
<!DOCTYPE html>
<html lang="en">
<head>
<meta charset="utf-8">
<title>Silver Kettle Consulting – Business Card</title>
<link rel="stylesheet" href="https://fonts.googleapis.com/css2?family=Open+Sans:wght@400;600;700&display=swap">
<style>
  :root {
    --green: #4a873e;
    --charcoal: #3a3a3c;
    --white: #ffffff;
    --soft-white: #f4f6f5;
    --page: #ffffff;
  }
  * { box-sizing: border-box; margin: 0; padding: 0; }
  html, body {
    width: 999px; height: 1200px; overflow: hidden;
    background: var(--page);
    font-family: "Open Sans", Arial, sans-serif;
  }
  .canvas { position: relative; width: 999px; height: 1200px; }
  .card {
    position: absolute; left: 17px; width: 965px;
    box-shadow: 4px 5px 6px rgba(0,0,0,0.45);
    overflow: hidden;
  }
  .card--front { top: 38px; height: 551px; background: var(--white); }
  .card--back { top: 616px; height: 550px; background: var(--green); }
  .card-shapes { position: absolute; inset: 0; }
  .text { position: absolute; white-space: nowrap; }

  .brand-mark { position: absolute; border-radius: 50%; }
  .card--front .brand-mark { left: 33px; top: 169px; width: 116px; height: 116px; background: var(--green); }
  .card--front .brand-name {
    left: 160px; top: 175px; font-size: 50px; line-height: 52px;
    font-weight: 600; color: var(--green);
  }
  .holder { left: 36px; top: 362px; color: var(--white); }
  .holder-name { font-size: 40px; font-weight: 700; line-height: 1; }
  .holder-role { font-size: 28px; font-weight: 400; line-height: 1; margin-top: 7px; }

  .address { left: 573px; top: 266px; font-size: 24px; line-height: 33px; color: var(--white); }
  .contacts { left: 616px; top: 409px; font-size: 24px; line-height: 33px; color: var(--white); }
  .contact-icons { position: absolute; left: 563px; top: 413px; }

  .card--back .brand-mark { left: 183px; top: 169px; width: 186px; height: 186px; background: var(--soft-white); }
  .card--back .brand-name {
    left: 386px; top: 181px; font-size: 82px; line-height: 86px;
    font-weight: 600; color: var(--soft-white);
  }
</style>
</head>
<body>
<main class="canvas">
  <section class="card card--front" aria-label="Card front">
    <svg class="card-shapes" width="965" height="551" viewBox="0 0 965 551">
      <polygon points="640,0 965,0 965,551 415,551" fill="var(--green)"/>
      <polygon points="548.5,224 965,224 965,362 492,362" fill="var(--charcoal)"/>
      <polygon points="0,331 448,331 391,469 0,469" fill="var(--charcoal)"/>
    </svg>
    <div class="brand-mark" aria-hidden="true"></div>
    <div class="text brand-name">Silver<br>Kettle</div>
    <div class="text holder">
      <div class="holder-name">Name Title</div>
      <div class="holder-role">designation</div>
    </div>
    <div class="text address">suit # 00, Lorem ipsum<br>Lorem Lorem ipsum</div>
    <svg class="contact-icons" width="30" height="96" viewBox="0 0 30 96" fill="none" stroke="var(--white)" stroke-width="2.4" stroke-linecap="round" stroke-linejoin="round">
      <path d="M5 3c-2 2-2 6 1 11s8 9 12 10c3 1 5 0 6-2l-4-4-3 2c-3-1-6-4-7-7l2-3z" fill="var(--white)" stroke="none"/>
      <path d="M16 3a8 8 0 0 1 7 7M16 7a4 4 0 0 1 3 3"/>
      <rect x="3" y="40" width="22" height="16" rx="1" fill="var(--white)" stroke="none"/>
      <path d="M3 41l11 8 11-8" stroke="var(--green)" stroke-width="2"/>
      <path d="M3 40l11-7 11 7"/>
      <circle cx="14" cy="81" r="11"/>
      <path d="M3 81h22M14 70c-5 6-5 16 0 22M14 70c5 6 5 16 0 22M5 75h18M5 87h18" stroke-width="1.6"/>
    </svg>
    <div class="text contacts">555-014-2837<br>maya@silverkettle.com<br>www.silverkettle.com</div>
  </section>

  <section class="card card--back" aria-label="Card back">
    <div class="brand-mark" aria-hidden="true"></div>
    <div class="text brand-name">Silver<br>Kettle</div>
  </section>
</main>
</body>
</html>
```